“The Future” Spring Fair Poster

We are putting together a school and community fair. We need a poster designed to advertise the event and give some important information to would be attendees. We’d like the poster graphics to evoke a minimalistic and futuristic aesthetic, be bold, yet fun! We will printing the posters, so we will need for them to be at high resolution and ready to send to print.

Target Market(s)

Students, Parents, and Community members

Industry/Entity Type

School

Font styles to use
Sans Serif

Colors
33a6d7
fabb78
9d9d9d
ffffff
1b1b1b
33b8a4

Requirements
Must have
• The Future
• Birch & Harbor Spring Fair 2018
• Friday, May 18th
• 5:00-9:00pm
• Tickets Will Be Available at Select Pick up & Drop Off Times
• Come Enjoy a Futuristic Evening of Food, Music, Entertainment, & Fun!
Nice to have
• We’d love to see a bold and graphic poster with a futuristic feel!
• See the sample image below from previous event poster and additional images for mood and inspiration. Would love to see metallics (silver or metallic colors)

```html
<!DOCTYPE html>
<html lang="en">
<head>
<meta charset="utf-8">
<title>The Future – Birch &amp; Harbor Spring Fair 2018</title>
<link rel="stylesheet" href="https://fonts.googleapis.com/css2?family=Dancing+Script:wght@600&family=Didact+Gothic&family=Montserrat:wght@500;700&display=swap">
<style>
  :root {
    --page-bg: #e4e4e0;
    --paper: #ffffff;
    --rose: #e7739b;
    --rose-soft: #f6b9cc;
    --rose-mist: #fbe2ea;
    --teal: #33b8a4;
    --grey: #6f6f6f;
    --ink: #3a3a3a;
    --band: #1b1b1b;
  }
  * { margin: 0; padding: 0; box-sizing: border-box; }
  html, body { width: 1200px; height: 801px; overflow: hidden; }
  body {
    background: var(--page-bg);
    position: relative;
    font-family: "Didact Gothic", sans-serif;
  }
  .poster {
    position: absolute;
    left: 340px;
    top: 18px;
    width: 520px;
    height: 765px;
    background: var(--paper);
    overflow: hidden;
    text-align: center;
  }
  .poster__title {
    position: absolute;
    top: 34px;
    left: 0;
    width: 100%;
    font-family: "Dancing Script", cursive;
    font-weight: 600;
    font-size: 84px;
    line-height: 1;
    color: var(--rose);
  }
  .poster__subtitle {
    position: absolute;
    top: 136px;
    left: 0;
    width: 100%;
    font-size: 26px;
    color: var(--grey);
    letter-spacing: 0.2px;
  }
  .poster__meadow {
    position: absolute;
    left: 0;
    top: 310px;
    width: 100%;
    height: 396px;
    background:
      radial-gradient(ellipse 60% 40% at 50% 35%, rgba(255,255,255,0.95), rgba(255,255,255,0) 70%),
      linear-gradient(180deg, rgba(255,255,255,0) 0%, var(--rose-mist) 35%, var(--rose-soft) 80%, #f3a6bd 100%);
  }
  .poster__wreath {
    position: absolute;
    left: 90px;
    top: 190px;
    width: 320px;
    height: 335px;
    border-radius: 50%;
    background: radial-gradient(circle, rgba(255,255,255,0) 58%, rgba(246,185,204,0.55) 62%, rgba(231,115,155,0.55) 66%, rgba(246,185,204,0.45) 71%, rgba(255,255,255,0) 78%);
  }
  .event-details {
    position: absolute;
    top: 312px;
    left: 0;
    width: 500px;
  }
  .event-details__date {
    font-family: "Montserrat", sans-serif;
    font-weight: 700;
    font-size: 19px;
    color: var(--rose);
  }
  .event-details__time {
    margin-top: 6px;
    font-size: 22px;
    color: var(--teal);
  }
  .event-details__tickets {
    margin-top: 8px;
    font-size: 13.5px;
    line-height: 1.3;
    color: var(--ink);
  }
  .poster__band {
    position: absolute;
    left: 0;
    bottom: 0;
    width: 100%;
    height: 59px;
    background: var(--band);
    padding-top: 12px;
  }
  .poster__band-headline {
    font-family: "Montserrat", sans-serif;
    font-weight: 700;
    font-size: 17.5px;
    color: #ffffff;
    line-height: 1.1;
  }
  .poster__band-list {
    margin-top: 3px;
    font-family: "Montserrat", sans-serif;
    font-weight: 500;
    font-size: 13px;
    color: var(--rose);
    word-spacing: 1px;
  }
</style>
</head>
<body>
  <main class="poster">
    <div class="poster__meadow" role="img" aria-label="Soft pink watercolour meadow with trees, tall grass and flowers"></div>
    <div class="poster__wreath" role="img" aria-label="Round wreath of pink blossoms and butterflies"></div>

    <h1 class="poster__title">The Future</h1>
    <p class="poster__subtitle">Birch &amp; Harbor Spring Fair 2018</p>

    <section class="event-details">
      <p class="event-details__date">FRIDAY, MAY 18TH</p>
      <p class="event-details__time">5:00-9:00pm</p>
      <p class="event-details__tickets">Tickets Will Be Available at<br>Select Pick up &amp; Drop Off Times</p>
    </section>

    <footer class="poster__band">
      <p class="poster__band-headline">COME ENJOY A FUTURISTIC EVENING OF</p>
      <p class="poster__band-list">FOOD | MUSIC | ENTERTAINMENT | FUN</p>
    </footer>
  </main>
</body>
</html>
```